Surgery Office Letterhead Design

I'm seeking new letterhead that will comprise all of our office locations and logo and other applicable information, per the following:

Office Locations:

Lakemont Institute for Jaw & Face Surgery at Cleburne
347 Hazelpine Court
Ashford, Texas 76120
Phone 817.382.4706
Fax 817.382.9034

Lakemont Institute for Jaw & Face Surgery at Stephenville
518 Willowgate Boulevard
Millbrook, Texas 76455
Phone 254.563.2781
Fax 254.563.2789

Lakemont Institute for Jaw & Face Surgery at Belton
739 West 9th Avenue
Carrow, Texas 76588
Phone 254.871.4035
Fax 254.871.4042

Other Info to include:

www.lakemontjawface.com
hello@lakemontjawface.com

Industry/Entity Type

Medical

Font styles to use
Serif
Sans Serif

Requirements
Must have
• See Project Description

```html
<!DOCTYPE html>
<html lang="en">
<head>
<meta charset="utf-8">
<title>Lakemont Institute Letterhead</title>
<link rel="stylesheet" href="https://fonts.googleapis.com/css2?family=Roboto:wght@300;400;500&display=swap">
<style>
  :root {
    --backdrop: #e6e4e1;
    --paper: #ffffff;
    --navy: #24406b;
    --brand: #2c3f66;
    --body-ink: #5a5a5a;
    --heading-ink: #4a4a4a;
    --detail-ink: #6a6a6a;
    --rule: #c9c9c9;
    --signature-tone: #e4e4e6;
  }
  * { margin: 0; padding: 0; box-sizing: border-box; }
  html, body {
    width: 1200px; height: 1000px; overflow: hidden;
    background: var(--backdrop);
    font-family: "Roboto", Arial, sans-serif;
  }
  .letterhead {
    position: absolute; left: 281px; top: 51px;
    width: 636px; height: 900px;
    background: var(--paper);
    box-shadow: 0 2px 10px rgba(0,0,0,0.12);
  }
  .brand {
    position: absolute; left: 37px; top: 42px;
    display: flex; align-items: center; gap: 10px;
    color: var(--brand); font-weight: 500;
  }
  .brand-dot { width: 14px; height: 14px; border-radius: 50%; background: var(--brand); }
  .brand-name { font-size: 19px; line-height: 21px; letter-spacing: 0.5px; text-transform: uppercase; }
  .brand-name small { display: block; font-size: 10px; line-height: 12px; letter-spacing: 0.3px; }
  .letter-body {
    position: absolute; left: 37px; top: 184px; width: 563px;
    color: var(--body-ink); font-weight: 300;
    font-size: 14.2px; line-height: 18px;
  }
  .salutation { margin-bottom: 19px; }
  .paragraph { margin-bottom: 18px; }
  .paragraph .line {
    display: block; white-space: nowrap;
    text-align: justify; text-align-last: justify;
  }
  .paragraph .line--last { text-align-last: left; }
  .signature {
    position: absolute; left: 37px; top: 638px;
    width: 138px; height: 36px;
    background: linear-gradient(90deg, var(--signature-tone), #f3f3f4);
    border-radius: 3px;
  }
  .office-block {
    position: absolute; left: 37px; top: 770px; width: 570px; height: 80px;
  }
  .office-label {
    position: absolute; left: 0; top: 32px;
    font-size: 12.5px; color: var(--navy); font-weight: 400;
  }
  .office-divider {
    position: absolute; left: 110px; top: 2px; width: 1px; height: 70px;
    background: var(--rule);
  }
  .office {
    position: absolute; top: 0;
    font-style: normal;
    font-size: 12.3px; line-height: 15px; color: var(--detail-ink); font-weight: 300;
    white-space: nowrap;
  }
  .office h3 { font-size: 12.5px; line-height: 15px; font-weight: 500; color: var(--heading-ink); }
  .office--ashford { left: 127px; }
  .office--millbrook { left: 274px; }
  .office--carrow { left: 444px; }
  .contact-band {
    position: absolute; left: 0; bottom: 0; width: 100%; height: 36px;
    background: var(--navy); color: #fff;
    display: flex; align-items: center; justify-content: center; gap: 8px;
    font-size: 12.5px; font-weight: 400;
  }
</style>
</head>
<body>
<main class="letterhead">
  <header class="brand">
    <span class="brand-dot"></span>
    <div class="brand-name">Lakemont Institute<small>for Jaw &amp; Face Surgery</small></div>
  </header>

  <section class="letter-body">
    <p class="salutation">Dear Lakemont,</p>
    <p class="paragraph">
      <span class="line">Lorem ipsum dolor sit amet, consectetur adipisicing elit, sed do eiusmod tempor</span>
      <span class="line">incididunt ut labore et dolore magna aliqua. Ut enim ad minim veniam, quis nos-</span>
      <span class="line">trud exercitation ullamco laboris nisi ut aliquip ex ea commodo consequat. Duis</span>
      <span class="line">aute irure dolor in reprehenderit in voluptate velit esse cillum dolore eu fugiat nulla</span>
      <span class="line">pariatur. Excepteur sint occaecat cupidatat non proident, sunt in culpa qui officia</span>
      <span class="line">deserunt mollit anim id est laborum.danken, der vor seiner Selbständigkeit bereits</span>
      <span class="line line--last">langjährige berufliche Erfahrung in der Immobilienwirtschaft sammeln konnte.</span>
    </p>
    <p class="paragraph">
      <span class="line">Lorem ipsum dolor sit amet, consectetur adipisicing elit, sed do eiusmod tempor</span>
      <span class="line">incididunt ut labore et dolore magna aliqua. Ut enim ad minim veniam, quis nos-</span>
      <span class="line">trud exercitation ullamco laboris nisi ut aliquip ex ea commodo consequat. Duis</span>
      <span class="line">aute irure dolor in reprehenderit in voluptate velit esse cillum dolore eu fugiat nulla</span>
      <span class="line">pariatur. Excepteur sint occaecat cupidatat non proident, sunt in culpa qui officia</span>
      <span class="line">deserunt mollit anim id est laborum.danken, der vor seiner Selbständigkeit bereits</span>
      <span class="line line--last">langjährige berufliche Erfahrung in der Immobilienwirtschaft sammeln konnte.</span>
    </p>
    <p class="paragraph">
      <span class="line">Lorem ipsum dolor sit amet, consectetur adipisicing elit, sed do eiusmod tempor</span>
      <span class="line">incididunt ut labore et dolore magna aliqua. Ut enim ad minim veniam, quis nos-</span>
      <span class="line">trud exercitation ullamco laboris nisi ut aliquip ex ea commodo consequat. Duis</span>
      <span class="line">aute irure dolor in reprehenderit in voluptate velit esse cillum dolore eu fugiat nulla</span>
      <span class="line line--last">pariatur.</span>
    </p>
  </section>

  <div class="signature" role="img" aria-label="Handwritten signature"></div>

  <section class="office-block">
    <p class="office-label">Office Locations</p>
    <span class="office-divider"></span>
    <address class="office office--ashford">
      <h3>Ashford</h3>
      347 Hazelpine Court<br>Ashford, Texas 76120<br>P : 817.382.4706<br>F : 817.382.9034
    </address>
    <address class="office office--millbrook">
      <h3>Millbrook</h3>
      518 Willowgate Boulevard<br>Millbrook, Texas 76455<br>P : 254.563.2781<br>F : 254.563.2789
    </address>
    <address class="office office--carrow">
      <h3>Carrow</h3>
      739 West 9th Avenue<br>Carrow, Texas 76588<br>P : 254.871.4035<br>F : 254.871.4042
    </address>
  </section>

  <footer class="contact-band">
    <span>hello@lakemontjawface.com</span><span>|</span><span>www.lakemontjawface.com</span>
  </footer>
</main>
</body>
</html>
```